Re-design a training handout - Pathway Keystone

We need a graphic design for a training workbook for leaders to use in a workshop and as a journal.
It is two A3 double sided with fold lines and content already laid out. It is dull & does not capture imagination.

We want it to be something a leader gets as part of a program and cannot not wait to begin filing out the blank sections.
We are calling it a leader "blue print".
It needs to be in Adobe Indesign5 (so we can improve it ourselves over the coming months.
We will send the Indesign file with everything already done EXCEPT the magic of a great layout.
A sample of ONE page (of Four) has been attached. It is page with the most writing.

Reason: I have provided a guarantee to pay and answered some questions which will help. A couple of designers requested extra information and guidance. Thanks again - there will be no further extension. Kind regards. Tom

Target Market(s)

Leaders and executives of team from 10 to 500

Industry/Entity Type

Graphic Design

Requirements
Must have
• Indesign5
work within the A3 with the fold lines already indicated
Be able to written on in the blank or line sections.
Keep the same text.

```html
<!DOCTYPE html>
<html lang="en">
<head>
<meta charset="utf-8">
<title>Pathway Keystone – Leader Workbook Spread</title>
<link href="https://fonts.googleapis.com/css2?family=Tinos:wght@400;700&display=swap" rel="stylesheet">
<style>
  :root {
    --ink: #1a56a6;
    --paper: #dbe9f7;
    --white: #ffffff;
    --stage: #000000;
    --orb-dark: #2b47a0;
    --orb-light: #eef1fa;
  }
  * { box-sizing: border-box; margin: 0; padding: 0; }
  html, body { width: 1200px; height: 900px; overflow: hidden; background: var(--stage); }
  body { position: relative; font-family: "Tinos", "Times New Roman", serif; font-weight: 700; color: var(--ink); }

  .spread { position: absolute; left: 34px; top: 50px; width: 1132px; height: 800px; }
  .page { position: absolute; top: 0; height: 800px; background: var(--paper); }
  .page-left { left: 0; width: 566px; }
  .page-right { left: 647px; width: 485px; }
  .spine { position: absolute; left: 566px; top: 0; width: 81px; height: 800px; background: var(--ink);
    display: flex; align-items: center; justify-content: center; }
  .spine-title { writing-mode: vertical-rl; transform: rotate(180deg); color: var(--white);
    font-size: 62px; letter-spacing: 2px; line-height: 1; white-space: nowrap; }

  .abs { position: absolute; }
  .tag { position: absolute; background: var(--ink); color: var(--white); font-size: 11px;
    display: flex; align-items: center; justify-content: center; }
  .dots { position: absolute; height: 0; border-top: 2px dotted var(--ink); }

  /* metrics */
  .metric-label { position: absolute; top: 27px; width: 135px; height: 27px; background: var(--ink);
    color: var(--white); font-size: 14px; display: flex; align-items: center; justify-content: center; }
  .metric-col { position: absolute; top: 28px; width: 56px; text-align: center; font-size: 11px; line-height: 13px; }
  .orbs { position: absolute; left: 0; top: 0; }

  /* action plan */
  .plan { position: absolute; left: 27px; top: 235px; width: 525px; height: 537px; background: var(--ink); border-radius: 14px; }
  .plan-title { position: absolute; left: 32px; top: 5px; color: var(--white); font-size: 14px; }
  .plan-table { position: absolute; left: 14px; top: 26px; width: 497px; height: 511px; background: var(--white);
    border-collapse: collapse; table-layout: fixed; }
  .plan-table th { height: 27px; font-size: 11px; text-align: left; border-bottom: 1px solid var(--ink); }
  .plan-table th.when { text-align: center; }
  .plan-table th.what { padding-left: 41px; }
  .plan-table td { height: 81px; border-bottom: 1px solid var(--ink); }
  .plan-table tr:last-child td { border-bottom: none; }
  .plan-table .when { width: 102px; border-right: 1px solid var(--ink); }

  .footer { position: absolute; bottom: 6px; font-size: 11px; }

  /* right page */
  .card { position: absolute; background: var(--white); border: 3px solid var(--ink); border-radius: 14px; }
  .card .tag { top: -2px; width: 135px; height: 19px; }
  .lines { position: absolute; display: flex; flex-direction: column; gap: 25px; }
  .lines span { display: block; border-top: 2px dotted var(--ink); }
</style>
</head>
<body>
<div class="spread">

  <section class="page page-left">
    <div class="metric-label" style="left:27px">PEOPLE METRIC</div>
    <div class="metric-col" style="left:175px">My<br>Baseline</div>
    <div class="metric-col" style="left:228px">My<br>Target</div>
    <div class="metric-label" style="left:289px">PEOPLE METRIC</div>
    <div class="metric-col" style="left:437px">My<br>Baseline</div>
    <div class="metric-col" style="left:491px">My<br>Target</div>

    <div class="dots" style="left:27px;top:93px;width:135px"></div>
    <div class="dots" style="left:27px;top:147px;width:135px"></div>
    <div class="dots" style="left:27px;top:201px;width:135px"></div>
    <div class="dots" style="left:289px;top:93px;width:135px"></div>
    <div class="dots" style="left:289px;top:147px;width:135px"></div>
    <div class="dots" style="left:289px;top:201px;width:135px"></div>

    <svg class="orbs" width="566" height="240" aria-hidden="true">
      <defs>
        <linearGradient id="orb-fill" x1="0" x2="1">
          <stop offset="0" stop-color="var(--orb-dark)"/>
          <stop offset="1" stop-color="var(--orb-light)"/>
        </linearGradient>
        <linearGradient id="orb-ring" x1="0" x2="1">
          <stop offset="0" stop-color="var(--orb-light)"/>
          <stop offset="1" stop-color="#4a63b4"/>
        </linearGradient>
      </defs>
      <g stroke="url(#orb-ring)" stroke-width="4" fill="url(#orb-fill)">
        <circle cx="203" cy="94" r="18"/><circle cx="256" cy="94" r="18"/>
        <circle cx="203" cy="148" r="18"/><circle cx="256" cy="148" r="18"/>
        <circle cx="203" cy="202" r="18"/><circle cx="256" cy="202" r="18"/>
        <circle cx="465" cy="94" r="18"/><circle cx="519" cy="94" r="18"/>
        <circle cx="465" cy="148" r="18"/><circle cx="519" cy="148" r="18"/>
        <circle cx="465" cy="202" r="18"/><circle cx="519" cy="202" r="18"/>
      </g>
    </svg>

    <div class="plan">
      <div class="plan-title">MY ACTION PLAN</div>
      <table class="plan-table">
        <tr><th class="when">WHEN</th><th class="what">WHAT</th></tr>
        <tr><td class="when"></td><td></td></tr>
        <tr><td class="when"></td><td></td></tr>
        <tr><td class="when"></td><td></td></tr>
        <tr><td class="when"></td><td></td></tr>
        <tr><td class="when"></td><td></td></tr>
        <tr><td class="when"></td><td></td></tr>
      </table>
    </div>
    <div class="footer" style="right:29px">Northfield Learning 2013</div>
  </section>

  <div class="spine"><h1 class="spine-title">PATHWAY KEYSTONE</h1></div>

  <section class="page page-right">
    <div class="card" style="left:10px;top:28px;width:448px;height:52px"></div>

    <div class="card" style="left:13px;top:94px;width:189px;height:296px">
      <div class="tag" style="left:24px">HOW I WORK</div>
      <div class="lines" style="left:11px;top:50px;width:162px">
        <span></span><span></span><span></span><span></span><span></span><span></span><span></span><span></span><span></span>
      </div>
    </div>

    <div class="card" style="left:215px;top:94px;width:243px;height:296px">
      <div class="tag" style="left:51px">WHY?</div>
      <div class="lines" style="left:11px;top:50px;width:216px">
        <span></span><span></span><span></span><span></span><span></span><span></span><span></span><span></span><span></span>
      </div>
    </div>

    <div class="card" style="left:13px;top:406px;width:189px;height:216px">
      <div class="tag" style="left:24px"></div>
    </div>

    <div class="card" style="left:215px;top:406px;width:243px;height:216px">
      <div class="tag" style="left:51px">CORE VALUES</div>
      <div class="lines" style="left:11px;top:52px;width:216px">
        <span></span><span></span><span></span><span></span><span></span><span></span>
      </div>
    </div>

    <div class="card" style="left:13px;top:638px;width:445px;height:135px">
      <div class="tag" style="left:8px;width:161px;top:0">DEVELOPMENT PRIORITIES</div>
      <div class="lines" style="left:11px;top:51px;width:202px">
        <span></span><span></span><span></span>
      </div>
      <div class="lines" style="left:225px;top:51px;width:204px">
        <span></span><span></span><span></span>
      </div>
    </div>

    <div class="footer" style="right:30px">Northfield Learning 2013</div>
  </section>

</div>
</body>
</html>
```